Postcard Design

Bramble Circuit Holdings is a waste and Recycling company. We want to purchase recyclable materials from businesses. We would like to use the colors green and grey. The exact colors needed in this project are described below. We would like to have a picture of waste cardboard,a picture of money, and and the line- Are you getting top dollar for your Recyclables? After please put our logo and our phone number: 800.472.5196, our website (tindlepath.com),
and our email address: marguerite@tindlepath.com.

* Postcard must contain our logo. Please see buisness card for branding

Industry/Entity Type

It Company

Requirements
Must have
• This postcard must contain the logo and these colors:
Pantone: 576C & 418C

```html
<!DOCTYPE html>
<html lang="en">
<head>
<meta charset="UTF-8">
<title>Bramble Circuit Holdings – Postcard</title>
<link rel="stylesheet" href="https://fonts.googleapis.com/css2?family=Bebas+Neue&family=Open+Sans:wght@400;700&display=swap">
<style>
  :root {
    --green: #5c8727;
    --green-light: #6f9e32;
    --grey: #51534a;
    --white: #ffffff;
    --page: #2b2b2b;
    --card-tan: #c9a57a;
    --card-tan-light: #d4b38a;
    --cash: #c8cdb4;
    --cash-dark: #aab294;
  }
  * { margin: 0; padding: 0; box-sizing: border-box; }
  html, body { width: 1200px; height: 900px; overflow: hidden; }
  body {
    background: var(--page);
    display: flex; align-items: center; justify-content: center;
    font-family: "Open Sans", Arial, sans-serif;
  }
  .postcard {
    position: relative;
    width: 1000px; height: 680px;
    background: var(--white);
    overflow: hidden;
  }
  .band { position: absolute; inset: 0; }
  .band--green {
    background: var(--green);
    clip-path: polygon(0 36%, 22% 23%, 100% 23%, 100% 66%, 0 84%);
  }
  .band--grey {
    background: var(--grey);
    clip-path: polygon(0 79%, 100% 53%, 100% 100%, 0 100%);
  }
  .brand {
    position: absolute; top: 62px; right: 70px;
    display: flex; align-items: center; gap: 12px;
    font-weight: 700; font-size: 30px; color: var(--grey);
  }
  .brand__mark { width: 22px; height: 22px; background: var(--green); }
  .photo { position: absolute; }
  .photo--cardboard {
    left: 80px; top: 228px; width: 380px; height: 215px;
    background: radial-gradient(ellipse at 50% 50%, var(--card-tan-light) 0%, var(--card-tan) 50%, rgba(201,165,122,0) 70%);
  }
  .photo--money {
    left: 610px; top: 175px; width: 310px; height: 160px;
    background: radial-gradient(ellipse at 50% 50%, var(--cash) 0%, var(--cash-dark) 50%, rgba(170,178,148,0) 70%);
  }
  .headline {
    position: absolute; right: 45px; top: 418px;
    text-align: right; font-family: "Bebas Neue", Impact, sans-serif;
    font-weight: 400; line-height: 1;
  }
  .headline__lead { color: var(--green-light); font-size: 34px; letter-spacing: 1px; }
  .headline__main { color: var(--white); font-size: 72px; letter-spacing: 1px; }
  .contact {
    position: absolute; left: 45px; top: 548px; color: var(--white);
  }
  .contact__title {
    font-family: "Bebas Neue", Impact, sans-serif; font-weight: 400;
    font-size: 32px; letter-spacing: 1px; margin-bottom: 4px;
  }
  .contact__list { list-style: none; }
  .contact__item {
    display: flex; align-items: center; gap: 22px;
    font-size: 16px; height: 27px;
  }
  .contact__icon { width: 20px; height: 16px; flex: none; }
  .contact__item--upper { text-transform: uppercase; }
</style>
</head>
<body>
  <article class="postcard">
    <div class="band band--green"></div>
    <div class="band band--grey"></div>

    <div class="brand"><span class="brand__mark"></span>Bramble Circuit Holdings</div>

    <div class="photo photo--cardboard" role="img" aria-label="Pile of used cardboard boxes"></div>
    <div class="photo photo--money" role="img" aria-label="Hand holding a fanned stack of dollar bills"></div>

    <h1 class="headline">
      <span class="headline__lead">Are you getting top dollar for</span><br>
      <span class="headline__main">Your recyclables?</span>
    </h1>

    <section class="contact">
      <h2 class="contact__title">Contact Us</h2>
      <ul class="contact__list">
        <li class="contact__item">
          <svg class="contact__icon" viewBox="0 0 20 16"><path d="M5 1 L8 4 L6 6 Q8 10 12 11 L14 9 L17 12 L14 15 Q4 13 3 3 Z" fill="#6f9e32"/></svg>
          800.472.5196
        </li>
        <li class="contact__item">
          <svg class="contact__icon" viewBox="0 0 20 16"><rect x="1" y="2" width="18" height="12" fill="#6f9e32"/><path d="M1 2 L10 9 L19 2" fill="none" stroke="#51534a" stroke-width="1.5"/></svg>
          marguerite@tindlepath.com
        </li>
        <li class="contact__item contact__item--upper">
          <svg class="contact__icon" viewBox="0 0 20 16"><rect x="1.5" y="1" width="17" height="11" fill="none" stroke="#6f9e32" stroke-width="2"/><rect x="7" y="13" width="6" height="2" fill="#6f9e32"/></svg>
          tindlepath.com
        </li>
      </ul>
    </section>
  </article>
</body>
</html>
```